Premium men's gut health supplement needs a bottle label designed

We’re velnora - a premium men’s wellness brand focused on gut health. Our first product is a high-quality daily supplement designed to support digestion, regularity, and internal cleanliness. Backed by science and tailored for modern lifestyles, velnora is crafted in the UK and proudly LGBT-owned. It aims to resolve intimacy problems that gay men may experience due to poor digestion but also does not exclude any other orientation - other men may use it simply to improve their digestion.

velnora is for health-conscious men who value science-backed supplements and want to feel confident from the inside out. Many of our early adopters will be gay and bisexual men who prioritise gut health as part of their self-care, sexual, and hygiene routine, though the product is equally effective and appealing to anyone seeking premium digestive support.

The product is premium the target customer is male, not specific to one location but primary markets will be US, UK and EU.

I’d like a supplement bottle designed for velnora, our premium men’s gut health brand. The focus should be clean, slightly clinical, and minimal - inspired by brands like Quelrin and Darvo. The key element is the wordmark (velnora) on the front, with no additional logo or icon. Lowercase text and a strong, contemporary font are preferred.

The bottle should be aesthetically pleasing so that people are proud to display it on their shelf, instead of hiding it in a cupboard (like Quelrin, darvo, Pia Venturek, Morvanel etc)

Avoid anything that shows the product as being for LGBT, e.g., no rainbows, men holding hands etc.

The design should be premium, minimalist and not be busy or overwhelming.

I have uploaded a file called "Bottle" to give an idea of the type of container, but please ignore the colours and change as you see fit. This is just for reference for the type of bottle we'll use - all colours are customisable.

I have also uploaded some images for "style" reference, e.g., darvo, quelrin, pia venturek, etc for inspiration.

```html
<!DOCTYPE html>
<html lang="en">
<head>
<meta charset="utf-8">
<title>velnora — Daily Gut Health Supplement Label</title>
<link rel="stylesheet" href="https://fonts.googleapis.com/css2?family=Outfit:wght@700&family=Jost:wght@400&display=swap">
<style>
  :root {
    --backdrop: #161210;
    --peach-light: #ead6cb;
    --peach-mid: #d9bcae;
    --peach-deep: #bd9c8c;
    --label-white: #f1efee;
    --ink: #151515;
    --ink-soft: #2a2a2a;
    --fade-brown: #7a5e50;
    --fade-peach: #e3b9a4;
  }
  html, body {
    margin: 0;
    padding: 0;
    width: 1200px;
    height: 960px;
    overflow: hidden;
    background: var(--backdrop);
  }
  .canvas {
    position: relative;
    width: 1200px;
    height: 960px;
  }
  .label {
    position: absolute;
    left: 240px;
    top: 78px;
    width: 720px;
    height: 805px;
    overflow: hidden;
    background: linear-gradient(90deg,
      var(--peach-mid) 0%,
      var(--peach-deep) 40%,
      var(--peach-mid) 62%,
      var(--peach-light) 100%);
  }
  .label-wave {
    position: absolute;
    left: 0;
    top: 0;
    width: 720px;
    height: 805px;
  }
  .product-title {
    position: absolute;
    left: 92px;
    top: 78px;
    margin: 0;
    font-family: "Outfit", sans-serif;
    font-weight: 700;
    font-size: 94px;
    line-height: 127px;
    letter-spacing: 1px;
    text-transform: uppercase;
    background: linear-gradient(160deg,
      var(--ink) 0%,
      var(--ink) 52%,
      var(--fade-brown) 66%,
      var(--fade-peach) 82%,
      var(--peach-light) 100%);
    -webkit-background-clip: text;
    background-clip: text;
    color: transparent;
  }
  .product-title span { display: block; }
  .product-details {
    position: absolute;
    left: 98px;
    top: 602px;
    margin: 0;
    font-family: "Jost", sans-serif;
    font-weight: 400;
    font-size: 26px;
    line-height: 36px;
    color: var(--ink-soft);
  }
  .brand {
    position: absolute;
    left: 98px;
    top: 730px;
    display: flex;
    align-items: center;
    gap: 14px;
  }
  .brand-dot {
    width: 30px;
    height: 30px;
    border-radius: 50%;
    border: 2px solid var(--ink-soft);
    box-sizing: border-box;
  }
  .brand-name {
    font-family: "Jost", sans-serif;
    font-weight: 400;
    font-size: 32px;
    color: var(--ink-soft);
    line-height: 1;
  }
</style>
</head>
<body>
  <main class="canvas">
    <section class="label">
      <svg class="label-wave" viewBox="0 0 720 805" aria-hidden="true">
        <path d="M0,545 C12,505 30,488 48,494 C95,520 200,585 390,600 L720,602 L720,805 L0,805 Z" fill="var(--label-white)"/>
      </svg>
      <h1 class="product-title">
        <span>Daily</span>
        <span>Gut</span>
        <span>Health</span>
        <span>Supplement</span>
      </h1>
      <p class="product-details">
        daily gut health supplement<br>
        60 capsules | 30-day supply<br>
        crafted in the UK
      </p>
      <div class="brand">
        <span class="brand-dot"></span>
        <span class="brand-name">velnora</span>
      </div>
    </section>
  </main>
</body>
</html>
```